PSD Designs needed to give to my Developer

Hello, I need PSD files to give to my programmer for the creation of my new website. The website is for ZORVA lane, a new clothing company based in Chicago, IL. We sell womens, mens and kids fashion. We specialize in jackets, outerwear and sweaters, but we sell clothing from every category, I have someone working on the logo, so I can't include it for reference. However, I have included 2 reference sites as well as a PDF of how the 2 reference sites could be merged together. The main company color should be blue (hence the name ZORVA lane), and the overall feel of the site should be FUN. It should communicate: This is where you want to shop if you want a FUN, HAPPY experience. I need the Home Page file designed very quickly. Whoever is awarded this job will immediately continue working with me to design the other 8 pages. I will pay for all pages. The amount I am offering is for this one page only, and I will pay you additional to design all other 8 pages. Thank you for your time and I will be picking the best design so that we can immediately build a great relationship and work through the rest of the project.

Industry/Entity Type

Apparel Store

Number of Pages Required

1 page

Font styles to use
Sans Serif

Colors
33a6d7
0492cd
ffffff

Requirements
Must have
• I have included all notes in the project description so please check there. My project must communicate: Fun and Happy Design. Even tho I have chosen a few variations of blue below, I still want the designer to incorporate other colors as necessary to acheive the desired look.
Should not have
• It should have a boring, childish feel

```html
<!DOCTYPE html>
<html lang="en">
<head>
<meta charset="utf-8">
<title>ZORVA lane — Home</title>
<link href="https://fonts.googleapis.com/css2?family=Nunito:wght@400;700;800&display=swap" rel="stylesheet">
<style>
  :root{
    --blue:#0492cd;
    --blue-light:#33a6d7;
    --white:#ffffff;
    --ink:#4a4a4a;
    --dark:#222222;
    --card:#ececec;
    --rule:#e2e2e2;
    --log:#a8632f;
    --log-dark:#7a4322;
    --mustard:#c9953e;
    --coral:#e07a5c;
    --berry:#b8324a;
    --teal:#8fb8ad;
    --stone:#9a9490;
  }
  *{box-sizing:border-box;margin:0;padding:0}
  html,body{width:1040px;height:1200px;overflow:hidden;background:var(--white);font-family:"Nunito",sans-serif;color:var(--ink)}
  .page{position:relative;width:1040px;height:1200px}

  .tagline{position:absolute;left:140px;top:13px;font-size:11.5px;line-height:17px;color:var(--ink)}
  .tagline strong{font-size:14px;font-weight:700}
  .brand{position:absolute;left:0;width:1040px;top:16px;text-align:center;font-size:29px;font-weight:800;letter-spacing:3px;color:var(--blue)}
  .account{position:absolute;top:13px;font-size:11.5px;text-align:center;color:var(--ink)}
  .account svg{display:block;margin:4px auto 0}
  .account.join{left:770px}
  .account.bag{left:833px}

  .nav{position:absolute;top:74px;left:0;width:1040px;height:34px;background:var(--blue);display:flex;justify-content:center;align-items:center;padding-right:10px}
  .nav a{color:var(--white);text-decoration:none;font-size:11px;letter-spacing:.5px;display:flex;align-items:center;height:34px}
  .nav .sep{color:var(--white);font-size:9px;margin:0 14px}
  .nav a.active{background:var(--blue-light);padding:0 20px;margin-right:11px;height:32px;margin-top:4px}

  .hero{position:absolute;top:108px;left:0;width:1040px;height:448px;
    background:
      linear-gradient(180deg,rgba(255,255,255,0) 70%,rgba(60,40,30,.25) 100%),
      radial-gradient(ellipse 90px 160px at 340px 320px,rgba(224,90,110,.55),rgba(224,90,110,0)),
      radial-gradient(ellipse 80px 140px at 520px 250px,rgba(224,122,92,.65),rgba(224,122,92,0)),
      radial-gradient(ellipse 70px 110px at 700px 200px,rgba(184,50,74,.6),rgba(184,50,74,0)),
      radial-gradient(ellipse 110px 240px at 780px 330px,rgba(201,149,62,.7),rgba(201,149,62,0)),
      radial-gradient(ellipse 100px 220px at 290px 300px,rgba(143,184,173,.55),rgba(143,184,173,0)),
      radial-gradient(ellipse 90px 200px at 520px 330px,rgba(40,35,40,.45),rgba(40,35,40,0)),
      linear-gradient(90deg,var(--log-dark) 0%,var(--log) 14%,#c28250 26%,#d8c7b8 42%,#e4ddd6 52%,#c9bfb7 64%,var(--stone) 78%,#b5683a 86%,#c87d45 90%,#8d8580 100%);}
  .btn{position:absolute;width:130px;height:36px;background:var(--blue);color:var(--white);font-size:11.5px;font-weight:700;letter-spacing:.5px;display:flex;align-items:center;justify-content:center}
  .hero .btn{left:455px;top:216px}
  .dots{position:absolute;left:495px;top:424px;display:flex;gap:5px}
  .dots span{width:9px;height:9px;border-radius:50%;border:1.5px solid var(--white)}
  .dots span.on{background:var(--white)}

  .section-title{position:absolute;top:600px;width:1040px;text-align:center;color:var(--blue);font-size:14.5px;font-weight:700;letter-spacing:2px}
  .product{position:absolute;top:647px;width:239px;height:145px;background:var(--card);overflow:hidden}
  .product .shot{position:absolute;left:0;right:0;top:0;bottom:0}
  .p1 .shot{background:radial-gradient(ellipse 75px 110px at 120px 80px,#2f3a44 0%,#3c4650 55%,rgba(236,236,236,0) 100%)}
  .p2 .shot{background:radial-gradient(ellipse 78px 110px at 120px 80px,#6a5446 0%,#7d6656 55%,rgba(236,236,236,0) 100%)}
  .p3 .shot{background:radial-gradient(ellipse 75px 110px at 120px 80px,#2c3850 0%,#3a4560 55%,rgba(236,236,236,0) 100%)}
  .product .overlay{position:absolute;left:10px;top:11px;width:218px;height:123px;background:rgba(51,166,215,.82);display:flex;align-items:center;justify-content:center}
  .product .label{width:123px;height:36px;border:1.5px solid var(--white);color:var(--white);font-size:11px;font-weight:700;letter-spacing:.6px;display:flex;align-items:center;justify-content:center}
  .p1{left:141px}.p2{left:400px}.p3{left:659px}
  .products-btn{left:455px;top:817px}

  .news-band{position:absolute;top:894px;left:0;width:1040px;height:132px;
    background:
      radial-gradient(ellipse 150px 110px at 560px 90px,rgba(30,36,60,.75),rgba(30,36,60,0)),
      radial-gradient(ellipse 70px 60px at 360px 90px,rgba(120,125,135,.6),rgba(120,125,135,0)),
      linear-gradient(180deg,rgba(0,0,0,0) 8%,rgba(30,40,70,.6) 10%,rgba(0,0,0,0) 13%),
      linear-gradient(90deg,#4a4b55 0%,#56575f 25%,#5d5e66 45%,#4e4f58 65%,#5a5a60 100%)}
  .news{position:absolute;left:298px;top:986px;width:446px;height:92px;background:var(--blue);text-align:center}
  .news h2{margin-top:17px;font-size:14.5px;font-weight:400;letter-spacing:.6px;color:var(--white)}
  .news form{position:absolute;left:100px;top:41px;width:266px;height:32px;background:var(--white);display:flex}
  .news input{flex:1;border:0;padding-left:13px;font-family:inherit;font-style:italic;font-size:9.5px;color:#888;outline:0}
  .news button{width:100px;margin:2px;background:var(--blue-light);border:0;color:var(--white);font-family:inherit;font-weight:700;font-size:11px}

  .footer{position:absolute;top:1131px;left:0;width:1040px;border-top:1px solid var(--rule)}
  .copy{position:absolute;left:142px;top:13px;font-size:11px;font-weight:700;color:var(--dark);letter-spacing:.4px}
  .links{position:absolute;right:141px;top:13px;font-size:11px;color:var(--dark);letter-spacing:.3px}
  .links .sep{margin:0 10px}
</style>
</head>
<body>
<div class="page">
  <header>
    <p class="tagline">Pop-up your own ZORVA<br>Boulevard for ONLY <strong>$99</strong></p>
    <div class="brand">ZORVA LANE</div>
    <div class="account join">Join Now
      <svg width="16" height="16" viewBox="0 0 16 16" fill="none" stroke="#555" stroke-width="1"><circle cx="8" cy="8" r="7"/><path d="M2 8h8M7.5 5.5 10 8l-2.5 2.5"/></svg>
    </div>
    <div class="account bag">Shoping Bag
      <svg width="16" height="16" viewBox="0 0 16 16"><path d="M6 5V3.5a2 2 0 0 1 4 0V5" fill="none" stroke="#555" stroke-width="1.2"/><path d="M1.5 5h13l-1.3 9.5H2.8z" fill="#555"/></svg>
    </div>
  </header>

  <nav class="nav">
    <a class="active" href="#">HOME</a>
    <a href="#">GET TO KNOW US</a><span class="sep">I</span>
    <a href="#">WHY ZORVA?</a><span class="sep">I</span>
    <a href="#">HOST A POP-UP</a><span class="sep">I</span>
    <a href="#">BECOME A STYLIST</a>
  </nav>

  <section class="hero" role="img" aria-label="Photo of three smiling women in colourful cardigans, scarves and patterned skirts in front of a log cabin">
    <a class="btn">Shop Now</a>
    <div class="dots"><span></span><span></span><span></span><span class="on"></span></div>
  </section>

  <h2 class="section-title">OUR MAIN PRODUCTS</h2>
  <div class="product p1"><div class="shot" role="img" aria-label="Man wearing a dark jacket"></div><div class="overlay"><span class="label">JACKETS</span></div></div>
  <div class="product p2"><div class="shot" role="img" aria-label="Man wearing a wool overcoat"></div><div class="overlay"><span class="label">OUTERWEAR</span></div></div>
  <div class="product p3"><div class="shot" role="img" aria-label="Man wearing a knit sweater"></div><div class="overlay"><span class="label">SWEATERS</span></div></div>
  <a class="btn products-btn">Shop Now</a>

  <div class="news-band" role="img" aria-label="Photo of a young man in a dark sweater in a bright living room"></div>
  <section class="news">
    <h2>ENTER YOUR EMAIL ADDRESS</h2>
    <form><input type="text" placeholder="EMAIL ADDRESS"><button type="button">Subscribe</button></form>
  </section>

  <footer class="footer">
    <p class="copy">© 2018 Zorvalane. All Rights Reserved.</p>
    <p class="links">Terms<span class="sep">I</span>Sitemap<span class="sep">I</span>Privacy<span class="sep">I</span>Policy<span class="sep">I</span>Join our Network</p>
  </footer>
</div>
</body>
</html>
```